Small consulting business needs a website designed to highlight value and four offerings

My company is a dynamic consulting firm with four Core Offerings: Learning & Evaluation, Program Management, Facilitation & Coaching; Implementation & Transformation. Our mission is to facilitate organizational change and transformation, and to make space for creativity, joy, belonging, and trust. If done successfully, we grow to better understand ourselves, each other, and the work we do together.

I'd like the website to give a feeling of confidence and clarity. I want the colors to match or compliment my logo. I want to have three tabs - Our Clients, Our Services, and Government.

See attached Word document for additional content. My current website is www.BrightHarborGroup.com.

Some websites I'm inspired by:
https://www.quillmeadowworks.com
https://www.verolandpartners.com
https://tqvb.org

Some websites of people/groups in my field that I find uninspiring:
http://denisehollick.com
https://www.marrowfen.org

Target Market(s)

State and local government agencies, health tech, and corporate HR departments

Industry/Entity Type

public health, aging, government, health tech

Coding

Coded - Design and coding required

Number of Pages Required

4 page

Font styles to use
Other font styles liked:
• Calibri and Merriweather

Colors
0054AA
0677BA
7BADD7
CADEEF
E8F1F8
00AB8E
00BBA5
67D7C9
C6EFE9
E9F9F6
FFC000
F8CF3A
FAE287
FDF2CF
FEFAEE
F0912C
F2A743
F7CA91
FBE8D2
FDF5EE

Requirements
Must have
• Attached logo and content, water colors few, and photos.
Nice to have
• Real pictures, which I can provide to the chosen designer
Should not have
• AI generated characters or cartoons.

```html
<!DOCTYPE html>
<html lang="en">
<head>
<meta charset="utf-8">
<title>Bright Harbor Group</title>
<link rel="stylesheet" href="https://fonts.googleapis.com/css2?family=Libre+Baskerville:wght@400;700&family=Montserrat:wght@400;500;600;700&display=swap">
<style>
:root{
  --orange:#F0912C;
  --orange-soft:#F2A743;
  --yellow:#F8CF3A;
  --gold:#FFC000;
  --cream:#FFFCEF;
  --cream-deep:#FAE287;
  --teal:#00AB8E;
  --teal-dark:#0F5C55;
  --mint:#F1FBF8;
  --ink:#111111;
  --body:#444444;
  --muted:#555555;
  --rule:#D8D8D8;
  --serif:'Libre Baskerville', Georgia, serif;
  --sans:'Montserrat', Arial, sans-serif;
}
*{margin:0;padding:0;box-sizing:border-box}
html,body{width:1200px;height:2995px;overflow:hidden}
body{position:relative;background:#fff;font-family:var(--sans);color:var(--ink)}
.abs{position:absolute}
.center{left:0;width:1200px;text-align:center}

/* hero */
.hero{position:absolute;left:0;top:0;width:1200px;height:799px;background:var(--cream);overflow:hidden}
.deco-circle{position:absolute;border-radius:50%;background:#FBEEC4}
.brand{position:absolute;left:130px;top:20px;width:124px;text-align:center}
.brand-mark{width:36px;height:36px;border-radius:50%;background:var(--gold);margin:0 auto 10px}
.brand-name{font-family:var(--serif);font-size:14px;line-height:18px;color:var(--ink)}
.top-links{position:absolute;right:146px;top:14px;display:flex;align-items:center;gap:38px}
.clients-link{font-size:13px;color:var(--ink);display:flex;align-items:center;gap:5px}
.cta{display:block;width:157px;height:44px;border-radius:22px;background:linear-gradient(90deg,var(--yellow),var(--orange));color:#fff;font-weight:700;font-size:14px;line-height:44px;text-align:center;letter-spacing:.3px}
.nav{position:absolute;left:356px;top:73px;width:698px;border-top:1px solid #E9E3CF;padding-top:15px;display:flex;justify-content:space-between;font-size:15px;font-weight:500}
.nav .active{color:var(--teal)}
.hero-title{top:166px;font-family:var(--serif);font-weight:700;font-size:44px;line-height:60px}
.hero-title .accent{color:var(--orange)}
.hero-lede{top:300px;font-size:16.5px;line-height:32px;font-weight:500}
.ghost{top:500px;font-family:var(--serif);font-weight:700;font-size:66px;color:#E3EEDD;letter-spacing:1px}
.offer{position:absolute;font-size:25px;font-weight:500;letter-spacing:.5px}
.scroll{top:752px;font-size:12px}

/* sections */
.h2{font-family:var(--serif);font-weight:700;font-size:36px;color:var(--ink)}
.h2 .accent{color:var(--orange)}
.copy{font-size:14px;line-height:24px;color:var(--body)}
.photo{position:absolute;border-radius:50%}
.ring{box-shadow:0 10px 24px rgba(0,0,0,.08);border:6px solid #fff}

.band{position:absolute;left:0;top:1525px;width:1200px;height:239px;background:linear-gradient(90deg,#F9C83A,#F6B23E 45%,#F0912C);overflow:hidden}
.band-text{top:96px;font-size:33px;font-weight:700;color:#fff;letter-spacing:.5px}
.dots{position:absolute;left:538px;top:206px;display:flex;gap:8px}
.dots span{width:17px;height:5px;border-radius:3px;background:#fff}
.dots span.on{width:28px;background:var(--teal)}

.cat{font-size:22px;color:var(--teal);letter-spacing:.5px}
.cap{position:absolute;width:260px;text-align:center;font-size:14.5px;color:var(--muted)}

.why{position:absolute;left:0;top:2646px;width:1200px;height:349px;background:linear-gradient(180deg,#F4FCFA,#FFFFFF)}
.foot-nav{position:absolute;left:141px;top:2869px;width:913px;height:64px;border-top:1px solid var(--rule);border-bottom:1px solid var(--rule);display:flex;justify-content:space-between;align-items:center;padding:0 14px;font-size:15px;font-weight:500}
.foot-nav i{font-style:normal;color:var(--ink)}
.copyright{top:2958px;font-size:13px;color:var(--muted)}
</style>
</head>
<body>

<header class="hero">
  <div class="deco-circle" style="left:1102px;top:-60px;width:480px;height:480px"></div>
  <div class="deco-circle" style="left:-230px;top:290px;width:300px;height:300px"></div>

  <div class="brand">
    <div class="brand-mark"></div>
    <div class="brand-name">Bright Harbor<br>Group</div>
  </div>

  <div class="top-links">
    <span class="clients-link">
      <svg width="10" height="12" viewBox="0 0 10 12"><circle cx="5" cy="3" r="3" fill="#111"/><path d="M0 12c0-4 2-5.5 5-5.5s5 1.5 5 5.5z" fill="#111"/></svg>
      Our Clients
    </span>
    <span class="cta">CONTACT US</span>
  </div>

  <nav class="nav">
    <span class="active">Home</span><span>About Us</span><span>Four Core Offerings</span><span>Case Studies</span><span>Services</span><span>Government</span>
  </nav>

  <h1 class="abs center hero-title"><span class="accent">A Seat at the Table for Collaboration,</span><br>Learning &amp; Meaningful Change.</h1>
  <p class="abs center hero-lede">Bright Harbor Group is a dynamic consulting firm with four Core Offerings: Learning &amp; Evaluation,<br>Program Management, Facilitation &amp; Coaching; Implementation &amp; Transformation</p>

  <div class="abs center ghost">Here For You &amp; Your Team</div>

  <div class="photo" role="img" aria-label="Watercolor illustration of four interlocking puzzle pieces in a circle"
       style="left:437px;top:393px;width:326px;height:326px;background:radial-gradient(circle at 35% 40%,#E8C23A,#9AA83A 45%,#2F8A76 75%,#0F5C55)"></div>

  <span class="offer" style="left:153px;top:447px">Learning</span>
  <span class="offer" style="left:828px;top:447px">Implementation</span>
  <span class="offer" style="left:143px;top:679px">Facilitation</span>
  <span class="offer" style="left:776px;top:679px">Program Management</span>

  <div class="abs center scroll">Scroll Down<br>
    <svg width="10" height="8" viewBox="0 0 10 8"><path d="M2 2l3 3 3-3" fill="none" stroke="#111" stroke-width="1.3"/></svg>
  </div>
</header>

<section>
  <h2 class="abs center h2" style="top:860px">Our <span class="accent">Mission</span></h2>
  <p class="abs copy" style="left:150px;top:918px;width:900px;text-align:center">Our mission is to facilitate organizational change and transformation, and to make space for creativity, joy, belonging, and trust. If done successfully, we grow to better understand ourselves, each other, and the work we do together.</p>

  <div class="photo ring" role="img" aria-label="Watercolor illustration of overlapping circles" style="left:144px;top:992px;width:208px;height:208px;background:radial-gradient(circle,#D9B93E,#3E8C78 60%,#F3F1E6)"></div>
  <h2 class="abs center h2" style="top:1010px">Our <span class="accent">Vision</span></h2>
  <p class="abs copy" style="left:410px;top:1070px;width:380px;text-align:center">Our vision is to be part of a world where organizations and collaborators connect as human beings first. We envision a future where partners and colleagues strive for ongoing growth together.</p>
  <div class="photo" role="img" aria-label="Photo of colleagues meeting around an office table" style="left:844px;top:992px;width:208px;height:208px;background:linear-gradient(135deg,#6E8A8C,#C9B79A 55%,#3A4448)"></div>

  <div class="photo" role="img" aria-label="Photo of a team working together in a bright meeting room" style="left:144px;top:1250px;width:208px;height:208px;background:linear-gradient(135deg,#D9DCDD,#9AA3A8 50%,#4B4E52)"></div>
  <h2 class="abs center h2" style="top:1228px">Our <span class="accent">Value</span></h2>
  <p class="abs copy" style="left:408px;top:1286px;width:384px;text-align:center">We are the tranquility in chaos. The steady partner always at the table with you. We drive meaningful and measurable change, resulting in sustained progress towards key community outcomes and multi-sector initiatives. Our work produces values realignment, critical technical assistance, and develops strategic plans for innovative organizations ready to elevate their work.</p>
  <div class="photo ring" role="img" aria-label="Watercolor illustration of a radiating burst in teal and gold" style="left:844px;top:1250px;width:208px;height:208px;background:radial-gradient(circle,#ffffff 18%,#F2B53A 40%,#1F7A6C 70%,#ffffff)"></div>
</section>

<section class="band">
  <div class="abs center band-text">TURN BOLD VISIONS INTO PRACTICAL RESULTS</div>
  <div class="dots"><span class="on"></span><span></span><span></span><span></span><span></span></div>
</section>

<section>
  <h2 class="abs center h2" style="top:1835px">We <span class="accent">Collaborate</span> With</h2>
  <div class="abs center cat" style="top:1901px">NONPROFIT</div>

  <div class="photo" role="img" aria-label="Photo of a man working on a laptop in an office" style="left:143px;top:1963px;width:216px;height:216px;background:linear-gradient(135deg,#5B6770,#A99B82 55%,#3C4247)"></div>
  <div class="photo" role="img" aria-label="Photo of colleagues shaking hands" style="left:492px;top:1963px;width:216px;height:216px;background:linear-gradient(135deg,#8A9BA6,#3E6AA0 55%,#C8B9A4)"></div>
  <div class="photo" role="img" aria-label="Photo of a business meeting with documents" style="left:839px;top:1963px;width:216px;height:216px;background:linear-gradient(135deg,#4A4F55,#D8C9B3 50%,#2E3A4C)"></div>
  <div class="cap" style="left:121px;top:2197px">Large Scale Companies</div>
  <div class="cap" style="left:440px;top:2197px;width:320px">International Partnerships &amp; Organizations</div>
  <div class="cap" style="left:817px;top:2197px">State Government Agencies</div>

  <div class="abs center cat" style="top:2254px">CORPORATE</div>
  <div class="photo" role="img" aria-label="Photo of stacked hands in a team huddle" style="left:144px;top:2317px;width:216px;height:216px;background:linear-gradient(135deg,#C99A7A,#8C5E45 55%,#E4D4C6)"></div>
  <div class="photo" role="img" aria-label="Photo of a laughing group of friends outdoors" style="left:376px;top:2317px;width:216px;height:216px;background:linear-gradient(135deg,#6F8A4E,#B39A80 55%,#E9E2D8)"></div>
  <div class="photo" role="img" aria-label="Photo of a large team meeting at a long table" style="left:607px;top:2317px;width:216px;height:216px;background:linear-gradient(135deg,#B8BDC0,#5A6066 55%,#E2E2E0)"></div>
  <div class="photo" role="img" aria-label="Photo of two colleagues smiling at a laptop" style="left:839px;top:2317px;width:216px;height:216px;background:linear-gradient(135deg,#8A7560,#4F6FA0 55%,#EDE9E3)"></div>
  <div class="cap" style="left:122px;top:2549px">National &amp; Local Nonprofits</div>
  <div class="cap" style="left:354px;top:2549px">Foundations</div>
  <div class="cap" style="left:585px;top:2549px">Tribal Serving Organizations</div>
  <div class="cap" style="left:815px;top:2549px">Startups in Tech</div>
</section>

<footer class="why">
  <h2 class="abs center h2" style="top:46px"><span class="accent">Why</span> Us</h2>
</footer>
<p class="abs copy" style="left:146px;top:2747px;width:908px;text-align:center">Through our Core Offerings and guided by our founder’s traditional and nontraditional methods for engaging and steering a team, we create a sense of belonging, foster transparency, and help to build stronger relationships. Our approach helps to drive meaningful change so that organizations and initiatives can clear roadblocks and meet collective goals. Our team’s proven ability to transform conflict into opportunity will help to advance your organization and the communities you serve.</p>

<nav class="foot-nav">
  <span>Home</span><i>/</i><span>About Us</span><i>/</i><span>Four Core Offerings</span><i>/</i><span>Case Studies</span><i>/</i><span>Services</span><i>/</i><span>Our Clients</span><i>/</i><span>Governments</span><i>/</i><span>Contact Us</span>
</nav>
<div class="abs center copyright">Copyright© 2025 Bright Harbor Group &nbsp;|&nbsp; All Rights Reserved</div>

</body>
</html>
```